Product label design needed for an odor removal line of products.

I need a label designed for an odor removal product line. There are eight additional odor removal products that I will need labels designed for so the winner will have additional work from me. I would like each of those products to have a similar look and feel in each one. This contest is for one of the products. The Breezeward Pod 385 (would love a better name if you are so inclined -many people know what it is by the 385). The no smell formula does not mask odors, it eliminates odors at their source . Also Reduces Allergens! Simply open silver packet and place in dispenser. Great for use in cars, near pet beds or litter boxes, near diaper pails -anywhere odors are a problem. Lasts 60-90 days. Safe to use. Other uses: Nursing homes, hotel rooms, locker rooms, teenage boy rooms, basements... Eco Friendly! No VOC's or phthalates! Do not consume. Keep out of reach of children and pets. Replace every 60-90 days. I put the picture of my logo , the product as it is packaged and a picture of the actual product and the dispenser it will go in. the package is 4x5 in silver packet with .25 seam on the side and .5 seam on the top and bottom. (Dispenser will have a label with reorder information on it. to be designed later) You do not have to put all information provided on the label. It is to be used as you see fit. I tend to like clean, bold designs but am open to all options. Prefer not to use word air freshener.

Target Market(s)

Men and women between 30-65

Industry/Entity Type

Cleaning Product

Font styles to use
Sans Serif

Colors
acd136
9bcb3c
ffffff

Requirements
Must have
• ability for concept/look to be used for a laundry product, smaller odor elimination pouch, odor removing canister and spray as well
Nice to have
• I like greens but am open to designers to decide
Should not have
• word air freshener

```html
<!DOCTYPE html>
<html lang="en">
<head>
<meta charset="utf-8">
<title>Breezeward Pod 385 – Product Label</title>
<link rel="stylesheet" href="https://fonts.googleapis.com/css2?family=Oswald:wght@500;700&family=Montserrat:wght@500;600;700&display=swap">
<style>
  :root {
    --stage: #d1d2d4;
    --label-top: #eef4c4;
    --label-white: #ffffff;
    --green-light: #acd136;
    --green: #9bcb3c;
    --green-mid: #7cc144;
    --green-deep: #2f8a3f;
    --ribbon-teal: #bfe0dc;
    --charcoal: #5e5f63;
    --rule: #6b6c70;
    --ink: #55565a;
    --white: #ffffff;
  }
  * { box-sizing: border-box; margin: 0; padding: 0; }
  html, body {
    width: 1200px; height: 725px; overflow: hidden;
    background: var(--stage);
  }
  .stage { position: relative; width: 1200px; height: 725px; }

  .label {
    position: absolute; left: 335px; top: 62px;
    width: 531px; height: 600px; overflow: hidden;
    background: linear-gradient(180deg, var(--label-top) 0%, #f6f9e4 35%, var(--label-white) 62%);
  }

  .label__ribbons {
    position: absolute; left: 0; top: 20px; width: 531px; height: 380px;
    background: linear-gradient(165deg,
      rgba(172,209,54,0) 18%,
      rgba(155,203,60,0.55) 38%,
      rgba(124,193,68,0.35) 50%,
      rgba(191,224,220,0.45) 62%,
      rgba(255,255,255,0) 78%);
  }

  .brand {
    position: absolute; left: 0; top: 90px; width: 531px;
    display: flex; justify-content: center; align-items: center; gap: 10px;
  }
  .brand__dot {
    width: 22px; height: 22px; border-radius: 50%;
    background: var(--charcoal);
  }
  .brand__name {
    font-family: "Oswald", sans-serif; font-weight: 700;
    font-size: 34px; letter-spacing: 3px; color: var(--charcoal);
  }

  .title { position: absolute; left: 0; top: 0; }
  .title__word { font-family: "Oswald", sans-serif; font-weight: 700; }
  .title__badge-num { font-family: "Oswald", sans-serif; font-weight: 500; }

  .claims {
    position: absolute; left: 80px; top: 513px;
    display: flex; align-items: center; gap: 11px;
  }
  .claim {
    width: 45px; height: 45px; border-radius: 50%;
    background: var(--charcoal); color: var(--white);
    display: flex; flex-direction: column; align-items: center; justify-content: center;
    font-family: "Montserrat", sans-serif; font-weight: 500;
    font-size: 9px; line-height: 0.95; text-align: center;
    box-shadow: 0 1px 2px rgba(0,0,0,0.35);
  }
  .claim strong { font-weight: 700; font-size: 10px; }

  .usage {
    margin-left: 3px; width: 200px;
    border: 1px solid #b9babd; background: var(--white);
    font-family: "Montserrat", sans-serif; text-align: center; color: var(--ink);
  }
  .usage__replace { font-weight: 600; font-size: 11.5px; padding: 3px 0 2px; letter-spacing: 0.2px; }
  .usage__warning {
    background: var(--green-mid); color: var(--white);
    font-weight: 700; font-size: 6.4px; padding: 2px 0; letter-spacing: 0.2px;
  }
  .usage__consume { font-weight: 600; font-size: 9px; padding: 2px 0 3px; }
</style>
</head>
<body>
<main class="stage">
  <section class="label">
    <div class="label__ribbons" role="img" aria-label="Flowing green and pale teal smoke ribbons"></div>

    <div class="brand">
      <span class="brand__dot"></span>
      <span class="brand__name">CLEARHAVEN</span>
    </div>

    <svg class="title" width="531" height="600" viewBox="0 0 531 600">
      <defs>
        <linearGradient id="titleFill" x1="0" y1="0" x2="0" y2="1">
          <stop offset="0" stop-color="#8cc63f"/>
          <stop offset="0.5" stop-color="#6bb843"/>
          <stop offset="1" stop-color="#2f8a3f"/>
        </linearGradient>
        <linearGradient id="badgeFill" x1="0" y1="0" x2="0" y2="1">
          <stop offset="0" stop-color="#77787c"/>
          <stop offset="1" stop-color="#4f5054"/>
        </linearGradient>
      </defs>

      <line x1="84" y1="222" x2="447" y2="222" stroke="var(--rule)" stroke-width="2"/>
      <text class="title__word" x="84" y="380" font-size="196" textLength="363"
            lengthAdjust="spacingAndGlyphs" fill="url(#titleFill)"
            stroke="#ffffff" stroke-width="3" paint-order="stroke">BREEZEWARD</text>
      <line x1="84" y1="402" x2="447" y2="402" stroke="var(--rule)" stroke-width="2"/>

      <text class="title__word" x="84" y="472" font-size="72" textLength="230"
            lengthAdjust="spacingAndGlyphs" fill="url(#titleFill)"
            stroke="#ffffff" stroke-width="2" paint-order="stroke">POD</text>
      <circle cx="390" cy="444" r="47" fill="url(#badgeFill)" stroke="#ffffff" stroke-width="3"/>
      <text class="title__badge-num" x="390" y="466" font-size="60" text-anchor="middle"
            textLength="76" lengthAdjust="spacingAndGlyphs" fill="#ffffff">385</text>
      <line x1="84" y1="484" x2="447" y2="484" stroke="var(--rule)" stroke-width="2"/>
    </svg>

    <div class="claims">
      <div class="claim"><span>eco</span><span>friendly</span></div>
      <div class="claim"><span>no</span><strong>VOC'S</strong></div>
      <div class="claim"><span>safe</span><span>to use</span></div>
      <div class="usage">
        <p class="usage__replace">REPLACE EVERY 60-90 DAYS</p>
        <p class="usage__warning">KEEP OUT OF REACH OF CHILDREN AND PETS</p>
        <p class="usage__consume">DO NOT CONSUME</p>
      </div>
    </div>
  </section>
</main>
</body>
</html>
```